Kelvaro, The smart answer for charity drives

Kelvaro needs a simple Wordpress website development. The key message is that we have three wins in fundraising according to my services - win for theorganisation - win for the partner and win for the audience and the community.STYLE:- My business card is attached so the site colors could match with the card;- We love the style of this website: https://www.marenboltwick.co.nz/ because it is modern, minimalist, clean and easy to navigate. I am happy to have a similar parallax (scrolling) site as the reference samplePlease feature the following on the site:* INTRODUCTION (or About)* SERVICES* MY QUOTE* CONTACT US* PLAXTERN ( the contents are in the attached .rtf file - please message me if you are unable to open this document)Deliverables:- I would like a fully functioning (Coded) wordpress site

• Personable approach
• It is all about You (the other person who is approach my business)

```html
<!DOCTYPE html>
<html lang="en">
<head>
<meta charset="utf-8">
<title>Kelvaro — The smart answer for charity drives</title>
<link href="https://fonts.googleapis.com/css2?family=Montserrat:wght@300;400;600;700&family=Open+Sans:ital,wght@0,400;0,600;0,700;1,400&display=swap" rel="stylesheet">
<style>
:root{
  --ink:#1f1f1f;
  --dark:#222222;
  --footer:#2a2a2a;
  --pink:#efb8ad;
  --pink-deep:#e49a8c;
  --pink-soft:#f6d6cf;
  --grey:#f1f0ef;
  --text:#555555;
  --white:#ffffff;
}
*{box-sizing:border-box;margin:0;padding:0}
html,body{width:1200px;height:3068px;overflow:hidden}
body{position:relative;background:var(--white);font-family:"Open Sans",Arial,sans-serif;color:var(--text)}
.block{position:absolute;left:0;width:1200px}

/* Hero */
.hero{top:0;height:560px;background:var(--dark);overflow:hidden}
.hero__brand{position:absolute;left:64px;top:38px;font-family:"Montserrat",sans-serif;font-weight:300;font-size:64px;color:var(--white);letter-spacing:1px}
.hero__portrait{position:absolute;left:380px;top:0;width:540px;height:560px;background:radial-gradient(ellipse at 50% 38%,#c9a27e 0%,#8a6a4c 35%,#3a2e26 75%,var(--dark) 100%)}
.hero__mark{position:absolute;left:68px;top:388px;width:64px;height:64px;background:var(--pink)}
.hero__wins{position:absolute;left:148px;top:386px;list-style:none;color:var(--white);font-size:13px;line-height:22px}
.hero__curve{position:absolute;left:0;bottom:0;width:1200px;height:90px}

/* Services */
.services{top:560px;height:440px}
.section-title{font-family:"Montserrat",sans-serif;font-weight:700;color:var(--ink);text-align:center;letter-spacing:1px}
.services .section-title{position:absolute;top:68px;width:100%;font-size:46px}
.title-rule{display:block;width:160px;height:2px;background:var(--ink);margin:6px auto 0}
.services__band{position:absolute;top:130px;left:0;width:1200px;height:310px}
.services__cols{position:absolute;top:176px;left:120px;display:flex;gap:0}
.services__list{list-style:none;font-size:15px;color:var(--ink);line-height:38px}
.services__list:nth-child(1){width:380px}
.services__list:nth-child(2){width:352px}
.services__list li::before{content:"";display:inline-block;width:8px;height:8px;border-radius:50%;background:var(--ink);margin-right:18px;vertical-align:middle}

/* Introduction */
.intro{top:1000px;height:1180px}
.intro .section-title{margin-top:24px;font-size:44px}
.intro__lead{width:1000px;margin:34px auto 40px;font-weight:700;font-size:15px;color:var(--ink);line-height:24px;text-align:center}
.intro__body{width:1010px;margin:0 auto;font-size:13.5px;line-height:24px}
.intro__body p{margin-bottom:16px}
.signature{position:absolute;right:150px;top:1116px;text-align:left}
.signature__name{font-family:"Montserrat",sans-serif;font-weight:600;font-size:22px;color:var(--ink)}
.signature__role{font-size:12px;color:var(--pink-deep);margin-top:4px}

/* Quote */
.quote{top:2190px;height:280px}
.quote__text{position:absolute;top:118px;left:0;width:100%;text-align:center;font-style:italic;font-size:20px;line-height:36px;color:#777}

/* Contact */
.contact{top:2470px;height:290px}
.contact .section-title{margin-top:58px;font-size:46px}
.contact__form{display:flex;justify-content:center;gap:18px;margin-top:44px}
.field{width:290px;height:46px;border:1px solid #e3e3e3;border-radius:23px;padding-left:22px;font-size:13px;color:#aaa;display:flex;align-items:center}
.button{width:150px;height:46px;border-radius:23px;background:var(--pink);color:var(--white);font-size:14px;display:flex;align-items:center;justify-content:center}

/* Footer */
.footer{top:2760px;height:308px;background:var(--footer);color:#cfcfcf;font-size:13px}
.footer__col{position:absolute;top:56px}
.footer__copy{font-size:12px;color:#aaa}
.footer__name{margin-top:28px;font-weight:700;color:var(--white);font-size:15px}
.footer__creds{font-size:11px;color:#aaa;margin-top:4px}
.footer__brand{margin-top:36px;font-family:"Montserrat",sans-serif;font-weight:300;font-size:54px;color:var(--white)}
.footer h3{font-size:15px;font-weight:700;color:var(--white);margin-bottom:22px}
.contact-line{display:flex;align-items:flex-start;gap:14px;margin-bottom:16px;line-height:20px}
.contact-line svg{flex:none;margin-top:2px}
</style>
</head>
<body>

<header class="block hero">
  <div class="hero__portrait" role="img" aria-label="Portrait photograph of the managing director"></div>
  <div class="hero__brand">Kelvaro</div>
  <div class="hero__mark"></div>
  <ul class="hero__wins">
    <li>Win for the organisation</li>
    <li>Win for the partner</li>
    <li>Win for the audience and<br>the community</li>
  </ul>
  <svg class="hero__curve" viewBox="0 0 1200 90" preserveAspectRatio="none"><path d="M0 90 L0 40 Q600 -20 1200 60 L1200 90 Z" fill="#ffffff"/></svg>
</header>

<section class="block services">
  <h2 class="section-title">SERVICES<span class="title-rule"></span></h2>
  <svg class="services__band" viewBox="0 0 1200 310" preserveAspectRatio="none">
    <path d="M0 30 Q600 -20 1200 30 L1200 250 Q600 330 0 260 Z" fill="#efb8ad"/>
  </svg>
  <div class="services__cols">
    <ul class="services__list">
      <li>Fundraising Strategic Action Plans</li>
      <li>Marketing Plans</li>
      <li>Workshops on fundraising</li>
      <li>Evaluation on fundraising projects</li>
      <li>Funding applications</li>
    </ul>
    <ul class="services__list">
      <li>Commercial partnerships</li>
      <li>Giving Programmes</li>
      <li>Legacy Programmes</li>
      <li>Capital Projects Fundraising</li>
      <li>Feasibility Studies</li>
    </ul>
    <ul class="services__list">
      <li>Consultancy on fundraising</li>
      <li>Mentoring on fundraising</li>
    </ul>
  </div>
</section>

<section class="block intro">
  <h2 class="section-title">INTRODUCTION<span class="title-rule"></span></h2>
  <p class="intro__lead">I come from Greece where I completed my Bachelor in Political Science and International Studies. I continued my studies in UK, in Birmingham where I received a Master's Degree in Diplomacy.</p>
  <div class="intro__body">
    <p>Further education includes a fundraising certificate, a governance course for directors, a contract law paper and a workshop on strategic planning for community groups.</p>
    <p>I worked for the organising committee of a major international sporting event as Deputy Manager in the International Relations Department, a role that taught me how partners, sponsors and volunteers come together to deliver results.</p>
    <p>I moved to New Zealand at the end of the games. I worked at a city council as sponsorship manager of festivals and community events, moved to a regional netball body as commercial manager, became executive officer for a swimming club for two years, held contracts with my own sponsorship and marketing business, and later worked for a health charity, a housing trust and other organisations. Four years ago I worked for a city council as fundraising lead for major projects, exceeding a target of seven million dollars for a new sports hub and a children's playground.</p>
    <p>My most recent job before re-establishing my own business was Director of Philanthropy for a regional museum, where I was responsible for giving and legacy programmes and developed an innovative bequest programme.</p>
    <p>I hold New Zealand citizenship.</p>
    <p>I am passionate about my family, sport, enjoy music, cooking good food and travelling.</p>
    <p>I have had governance experience with community trusts, a local school board of trustees and as President of a cultural association in the city for five years. I am a current member of a national institute of directors and of a women on boards network.</p>
    <p>My greatest passion is people. I am grateful to all the teams that I worked with and the results that we achieved together. I always meet with potential partners to identify their objectives and outcomes, then tailor proposals to fit both their desires, the project's objectives and communities' interests. My approach is tailored and very personal. I believe this is the point of difference. I have developed strong relationships with funders, commercial businesses and donors during the years due to this approach.</p>
    <p>I am excited with projects that have an impact in the community and in our country.</p>
  </div>
  <div class="signature">
    <div class="signature__name">Mira Calloway-Venn</div>
    <div class="signature__role">Managing Director</div>
  </div>
</section>

<section class="block quote">
  <svg class="block" style="top:0;height:280px" viewBox="0 0 1200 280" preserveAspectRatio="none">
    <path d="M0 40 Q300 0 600 30 T1200 20 L1200 250 Q900 290 600 255 T0 260 Z" fill="#f1f0ef"/>
  </svg>
  <p class="quote__text">" I look forward to working with you and your team and together achieving<br>results that will make a difference where we live "</p>
</section>

<section class="block contact">
  <h2 class="section-title">CONTACT US<span class="title-rule"></span></h2>
  <div class="contact__form">
    <div class="field">Name</div>
    <div class="field">Email</div>
    <div class="button">Submit</div>
  </div>
</section>

<footer class="block footer">
  <div class="footer__col" style="left:64px">
    <div class="footer__copy">© 2019 Kelvaro</div>
    <div class="footer__name">Mira Calloway-Venn</div>
    <div class="footer__creds">MDipl. BIntS. BSc</div>
    <div class="footer__brand">Kelvaro</div>
  </div>
  <div class="footer__col" style="left:360px">
    <h3>We would love to hear from you</h3>
    <div class="contact-line">
      <svg width="14" height="18" viewBox="0 0 14 18"><path d="M7 0a7 7 0 0 0-7 7c0 5 7 11 7 11s7-6 7-11a7 7 0 0 0-7-7zm0 10a3 3 0 1 1 0-6 3 3 0 0 1 0 6z" fill="#efb8ad"/></svg>
      <span>42 Harbour Lane,<br>Pinecliff, 0712, Auckland</span>
    </div>
    <div class="contact-line">
      <svg width="14" height="16" viewBox="0 0 14 16"><path d="M3 0h3l1 4-2 1.5a9 9 0 0 0 3.5 4.5L10 8l4 1v3c0 1-1 2-2 2C5 14 0 9 0 2c0-1 1-2 3-2z" fill="#efb8ad"/></svg>
      <span>021 555 0147</span>
    </div>
    <div class="contact-line">
      <svg width="16" height="12" viewBox="0 0 16 12"><rect x="0.5" y="0.5" width="15" height="11" fill="none" stroke="#efb8ad"/><path d="M0.5 0.5 8 7l7.5-6.5" fill="none" stroke="#efb8ad"/></svg>
      <span>mira@kelvaro.co.nz</span>
    </div>
  </div>
  <div class="footer__col" style="left:700px">
    <h3>Plaxtern</h3>
    <div class="contact-line" style="width:300px">https://plaxtern.com/in/mira-calloway-venn-7731</div>
  </div>
</footer>

</body>
</html>
```